Professional Coaching Business Letterhead/Footer

I need a letterhead and email footer for my personal coaching business, Dale R Fenwick Professional Coaching. I send several attachments to new clients (such as welcome letter, fee structure, etc) and would like these pages to have my branding on them.
I prefer the black and gold/silver color scheme, and will attach my logo to be used. I'd like the overall impression to be upmarket/regal/professional.

One of the uploaded files is my business card, to give an idea of the style/feel I like. The others are vector files containing logo to be used.

Target Market(s)

Corporate managers, successful business people. 30-60 yrs old.

Industry/Entity Type

Business

Requirements
Must have
• Logo (DRF)
Nice to have
• Shield emblem around logo, some type of watermark.
Should not have
• The first uploaded file is my business card, intended to show style and colors- not to be used itself as the letterhead.

```html
<!DOCTYPE html>
<html lang="en">
<head>
<meta charset="utf-8">
<title>Dale R Fenwick Professional Coaching – Stationery</title>
<link href="https://fonts.googleapis.com/css2?family=Cinzel:wght@400&family=Source+Sans+3:wght@400&display=swap" rel="stylesheet">
<style>
  :root {
    --backdrop: #d8d5cf;
    --black: #000000;
    --paper-light: #ffffff;
    --paper-shade: #eeeeee;
    --gold: #c8b472;
    --gold-light: #e6d49a;
    --gold-deep: #b39c5a;
    --silver: #e4e4ea;
    --rule-grey: #a9a9b0;
    --white: #ffffff;
  }
  * { margin: 0; padding: 0; box-sizing: border-box; }
  html, body { width: 826px; height: 1200px; overflow: hidden; }
  body { background: var(--backdrop); position: relative; font-family: "Source Sans 3", sans-serif; }

  .letterhead {
    position: absolute; left: 27px; top: 32px; width: 760px; height: 984px;
    background: linear-gradient(160deg, var(--paper-light) 30%, var(--paper-shade) 100%);
    box-shadow: 0 2px 8px rgba(0,0,0,.25);
  }
  .letterhead__header {
    position: absolute; left: 0; top: 0; width: 100%; height: 128px;
    background: var(--black);
  }
  .brand { position: absolute; left: 50%; transform: translateX(-50%); text-align: center; }
  .brand__dot { display: block; margin: 0 auto; border-radius: 50%; background: var(--gold); }
  .brand__name {
    font-family: "Cinzel", serif; color: var(--silver); white-space: nowrap; letter-spacing: .02em;
  }
  .brand__rule { height: 1px; background: var(--gold); }
  .brand__tag {
    font-family: "Cinzel", serif; color: var(--silver); letter-spacing: .06em; white-space: nowrap;
  }

  .letterhead__header .brand { top: 22px; width: 196px; }
  .letterhead__header .brand__dot { width: 28px; height: 28px; }
  .letterhead__header .brand__name { font-size: 23px; margin-top: 16px; line-height: 1; }
  .letterhead__header .brand__rule { margin-top: 6px; }
  .letterhead__header .brand__tag { font-size: 11.5px; margin-top: 5px; }

  .letterhead__footer {
    position: absolute; left: 0; bottom: 0; width: 100%; height: 45px;
    background: linear-gradient(180deg, var(--gold-light), var(--gold-deep));
    border-top: 3px solid var(--rule-grey);
    display: flex; justify-content: center; align-items: center; gap: 12px;
    color: var(--white); font-size: 15.5px;
  }
  .contact { display: inline-flex; align-items: center; gap: 5px; white-space: nowrap; }
  .icon { width: 14px; height: 14px; flex: none; }

  .card {
    position: absolute; left: 166px; top: 1051px; width: 492px; height: 134px;
    background: var(--black); box-shadow: 0 2px 6px rgba(0,0,0,.25);
  }
  .card .brand { left: 166px; top: 14px; width: 164px; }
  .card .brand__dot { width: 26px; height: 26px; }
  .card .brand__name { font-size: 19px; margin-top: 26px; line-height: 1; }
  .card .brand__rule { margin-top: 5px; }
  .card__divider {
    position: absolute; left: 277px; top: 31px; width: 1px; height: 58px; background: #555;
  }
  .card__contacts {
    position: absolute; left: 291px; top: 28px; display: flex; flex-direction: column; gap: 3px;
    color: var(--white); font-size: 11.5px; line-height: 17px;
  }
  .card__contacts .icon { width: 11px; height: 11px; }
  .card__band {
    position: absolute; left: 0; bottom: 0; width: 100%; height: 24px;
    background: linear-gradient(90deg, var(--gold-light), var(--gold-deep));
    border-top: 2px solid var(--rule-grey);
    color: var(--white); font-size: 14px; text-align: center; line-height: 22px; letter-spacing: .02em;
  }
</style>
</head>
<body>
  <svg width="0" height="0" style="position:absolute">
    <defs>
      <symbol id="i-phone" viewBox="0 0 16 16">
        <circle cx="8" cy="8" r="7" fill="none" stroke="currentColor" stroke-width="1.2"/>
        <path d="M5.5 4.5c-.8.8-.6 3 1.3 4.9s4 2.1 4.8 1.3l-1.4-1.4-1 .6c-.8-.3-1.6-1.1-1.9-1.9l.6-1z" fill="currentColor"/>
      </symbol>
      <symbol id="i-mail" viewBox="0 0 16 16">
        <path d="M1.5 6.5 8 2l6.5 4.5V14h-13z" fill="currentColor"/>
        <path d="M1.5 6.5 8 10.5l6.5-4" fill="none" stroke="#000" stroke-opacity=".35" stroke-width="1"/>
      </symbol>
      <symbol id="i-web" viewBox="0 0 16 16">
        <g fill="none" stroke="currentColor" stroke-width="1.1">
          <circle cx="8" cy="8" r="6.5"/><ellipse cx="8" cy="8" rx="3" ry="6.5"/>
          <path d="M1.5 8h13M2.5 4.8h11M2.5 11.2h11"/>
        </g>
      </symbol>
    </defs>
  </svg>

  <section class="letterhead">
    <header class="letterhead__header">
      <div class="brand">
        <span class="brand__dot"></span>
        <div class="brand__name">DALE R FENWICK</div>
        <div class="brand__rule"></div>
        <div class="brand__tag">PROFESSIONAL COACHING</div>
      </div>
    </header>
    <footer class="letterhead__footer">
      <span class="contact"><svg class="icon"><use href="#i-phone"/></svg>503.418.2264</span>
      <span class="contact"><svg class="icon"><use href="#i-mail"/></svg>dale@dalerfenwick.com</span>
      <span class="contact"><svg class="icon"><use href="#i-web"/></svg>www.dalerfenwick.com</span>
    </footer>
  </section>

  <section class="card">
    <div class="brand">
      <span class="brand__dot"></span>
      <div class="brand__name">DALE R FENWICK</div>
      <div class="brand__rule"></div>
    </div>
    <div class="card__divider"></div>
    <div class="card__contacts">
      <span class="contact"><svg class="icon"><use href="#i-phone"/></svg>503.418.2264</span>
      <span class="contact"><svg class="icon" style="color:var(--gold)"><use href="#i-mail"/></svg>dale@dalerfenwick.com</span>
      <span class="contact"><svg class="icon" style="color:var(--gold)"><use href="#i-web"/></svg>www.dalerfenwick.com</span>
    </div>
    <div class="card__band">PROFESSIONAL COACHING</div>
  </section>
</body>
</html>
```